Restaurant needs a vertical banner for fried catfish

Our restaurant is looking for an eye-catching 78.75in. x 36in. vertical physical banner ad for our fried catfish. Photos for the fried catfish will be provided as a reference but we will also accept anything similar to the photo. We will be using the following as our receptacle: https://www.plankoria.example/banner-stand/retractable-banner-stands/
The design must incorporate the following flavor texts:
Fried Catfish
Always Fresh!
Made from Scratch
Hand-cut Fillets
The Best Catfish in Texas
Served with fries, hush puppies, and a 32oz fountain drink
Also available by the pound!
The final design should be creative, professional, and eye-catching for customers.
Updates
Colors
Designer to choose colors to be used in the design.
Requirements
Must have
- We are open to any and all design elements, albeit the 'flavor texts' should not overpower, but complement the fried catfish photo. 'Fried Catfish' can be used in lieu of a main title/logo.
Nice to have
- Transparent or textured backgrounds that can encompass any or all part of the banner such as a cutting board, shadows, abstract, etc to show depth are a plus.
- Use of vectors or objects such as ribbons or shapes to encapsulate the 'flavor texts' are also encouraged.

```html
<!DOCTYPE html>
<html lang="en">
<head>
<meta charset="utf-8">
<title>Fried Catfish – Vertical Banner</title>
<link href="https://fonts.googleapis.com/css2?family=Montserrat:wght@600;700;800;900&display=swap" rel="stylesheet">
<style>
  :root {
    --stage: #5e5e5e;
    --green-light: #13471f;
    --green-dark: #072712;
    --gold: #d99f48;
    --white: #ffffff;
    --callout-red: #a3151b;
    --pill-brown: #9b561d;
  }
  * { margin: 0; padding: 0; box-sizing: border-box; }
  html, body {
    width: 1200px; height: 717px; overflow: hidden;
    background: var(--stage);
  }
  .banner {
    position: absolute; left: 453px; top: 38px;
    width: 293px; height: 640px; overflow: hidden;
    background: radial-gradient(ellipse at 15% 20%, var(--green-light) 0%, #0d3818 45%, var(--green-dark) 100%);
    box-shadow: 6px 8px 14px rgba(0,0,0,.35);
    font-family: "Montserrat", sans-serif;
  }
  .food-photo { position: absolute; inset: 0; width: 293px; height: 640px; }
  .title {
    position: absolute; left: 25px; top: 25px;
    font-weight: 800; font-size: 54px; line-height: 41px; letter-spacing: -1px;
  }
  .title .fried { color: var(--white); display: block; }
  .title .catfish { color: var(--gold); display: block; }
  .title-rule {
    position: absolute; left: 27px; top: 117px; width: 219px; height: 2px;
    background: var(--white);
  }
  .tagline {
    position: absolute; left: 27px; top: 131px;
    color: var(--gold); font-weight: 700; font-size: 16px; letter-spacing: 3.2px;
  }
  .features {
    position: absolute; left: 27px; top: 166px;
    font-weight: 800; font-size: 22px; line-height: 19.5px; letter-spacing: -.3px;
  }
  .features .white { color: var(--white); display: block; }
  .features .gold { color: var(--gold); display: block; }
  .served {
    position: absolute; left: 28px; top: 271px;
    color: var(--white); font-weight: 600; font-size: 10.5px; line-height: 12px;
  }
  .best-callout {
    position: absolute; left: 168px; top: 452px; width: 96px; height: 96px;
    border-radius: 50%; background: var(--callout-red);
    box-shadow: 2px 3px 6px rgba(0,0,0,.4);
    display: flex; align-items: center; justify-content: center;
  }
  .best-callout-text {
    font-weight: 800; font-size: 12px; line-height: 15px;
    color: var(--white); text-align: center;
  }
  .pound-pill {
    position: absolute; left: 0; top: 588px; width: 259px; height: 30px;
    background: var(--pill-brown); border-radius: 0 15px 15px 0;
    color: var(--white); font-weight: 600; font-size: 13.5px;
    padding-left: 28px; line-height: 30px;
  }
</style>
</head>
<body>
  <section class="banner">
    <svg class="food-photo" viewBox="0 0 293 640" role="img" aria-label="Photo of fried catfish fillet plates with fries, hush puppies and tartar sauce">
      <defs>
        <radialGradient id="plateTones" cx="55%" cy="70%" r="70%">
          <stop offset="0%" stop-color="#b06a2a"/>
          <stop offset="45%" stop-color="#c9893e"/>
          <stop offset="75%" stop-color="#e2c58a"/>
          <stop offset="100%" stop-color="#f1ece2"/>
        </radialGradient>
      </defs>
      <path d="M170 165 Q230 160 255 175 L293 185 L293 455 Q260 520 210 540 Q150 560 90 545 Q30 530 0 520 L0 350 Q60 330 120 345 Q130 300 150 280 Q140 240 165 220 Q150 190 170 165 Z" fill="url(#plateTones)"/>
    </svg>

    <h1 class="title"><span class="fried">Fried</span><span class="catfish">Catfish</span></h1>
    <div class="title-rule"></div>
    <p class="tagline">ALWAYS FRESH!</p>
    <p class="features">
      <span class="white">Made from</span>
      <span class="white">Scratch</span>
      <span class="gold">Hand-cut</span>
      <span class="gold">Fillets</span>
    </p>
    <p class="served">Served with fries,<br>hush puppies,<br>and a 32oz<br>fountain drink</p>

    <div class="best-callout"><p class="best-callout-text">The Best<br>Catfish<br>in Texas</p></div>

    <div class="pound-pill">Also available by the pound!</div>
  </section>
</body>
</html>
```